Business Card Design Project

We need a redesign of our business card.
We are a Consulting Property Developer called The Selwick Group
Updates

Thank you all for submissions. Just waiting on managment to decide.

Thank you,

Dorinda

Industry/Entity Type

Business

Requirements
Must have
• we like having the SG a focus in the back ground or on the side
Selwick is our company colour

the wording - property development
and - premium accommodation

our website www.selwickgroup.com.au

persons name
title

p: 1300 582914 f: 1300 582917 m: 0419358027
PO Box 2817, Brackenvale Qld 4215
e: admin@selwickgroup.com.au

```html
<!DOCTYPE html>
<html lang="en">
<head>
<meta charset="utf-8">
<title>The Selwick Group – Business Cards</title>
<link rel="stylesheet" href="https://fonts.googleapis.com/css2?family=Jost:wght@400;500;700&display=swap">
<style>
  :root {
    --selwick: #8c1538;
    --ink-grey: #8b8d90;
    --rule-grey: #b9bbbe;
    --card: #f6f7f8;
    --backdrop: #e4e4e2;
    --ghost: #e6e7e9;
  }
  * { box-sizing: border-box; margin: 0; padding: 0; }
  html, body {
    width: 1200px; height: 774px; overflow: hidden;
    background: var(--backdrop);
    font-family: "Jost", sans-serif;
  }
  .sheet {
    position: relative; width: 1200px; height: 774px;
    display: flex; align-items: center; justify-content: center; gap: 40px;
  }
  .card {
    position: relative; width: 540px; height: 309px;
    background: var(--card); overflow: hidden;
    box-shadow: 0 6px 18px rgba(0,0,0,.12);
  }

  /* shared wordmark */
  .wordmark { display: flex; align-items: center; gap: 10px; }
  .wordmark__dot {
    border: 2px solid var(--ink-grey); border-radius: 50%;
  }
  .wordmark__name { color: var(--ink-grey); font-weight: 400; white-space: nowrap; }

  /* front */
  .card--front .wordmark { position: absolute; left: 30px; top: 34px; }
  .card--front .wordmark__dot { width: 32px; height: 32px; }
  .card--front .wordmark__name { font-size: 26px; }
  .card--front .wordmark-rule {
    position: absolute; left: 80px; top: 76px; width: 230px; height: 1px; background: var(--rule-grey);
  }
  .card--front .divider {
    position: absolute; left: 30px; right: 30px; top: 128px; height: 1px; background: var(--rule-grey);
  }
  .person { position: absolute; left: 30px; top: 160px; }
  .person__name { color: var(--selwick); font-weight: 700; font-size: 19px; }
  .person__title { color: var(--ink-grey); font-size: 12px; margin-top: 2px; margin-left: 8px; }

  .contacts {
    position: absolute; left: 30px; right: 24px; top: 222px;
    display: grid; grid-template-columns: auto auto auto; gap: 5px 14px;
    color: var(--ink-grey); font-size: 12px;
    border-top: 1px solid var(--rule-grey); padding-top: 8px;
  }
  .contacts__item { display: flex; align-items: center; gap: 6px; white-space: nowrap; }
  .contacts__item--wide { grid-column: span 2; }
  .contacts__icon { width: 11px; height: 11px; fill: var(--selwick); flex: none; }
  .band { position: absolute; left: 0; right: 0; bottom: 0; height: 9px; background: var(--selwick); }

  /* back */
  .ghost-mark {
    position: absolute; right: -40px; top: 40px; width: 300px; height: 300px;
    border-radius: 50%; border: 22px solid var(--ghost);
  }
  .card--back .wordmark { position: absolute; left: 40px; top: 84px; }
  .card--back .wordmark__dot { width: 46px; height: 46px; }
  .card--back .wordmark__name { font-size: 40px; }
  .card--back .wordmark-rule {
    position: absolute; left: 106px; top: 146px; width: 360px; height: 1px; background: var(--rule-grey);
  }
  .tagline {
    position: absolute; left: 40px; bottom: 40px;
    color: var(--selwick); font-size: 12.5px; letter-spacing: .24em; text-transform: uppercase;
  }
  .tagline__sep { margin: 0 12px; }
</style>
</head>
<body>
<main class="sheet">

  <section class="card card--front" aria-label="Business card front">
    <div class="wordmark">
      <span class="wordmark__dot"></span>
      <span class="wordmark__name">The Selwick Group</span>
    </div>
    <div class="wordmark-rule"></div>
    <div class="divider"></div>

    <div class="person">
      <p class="person__name">Corwin Hale</p>
      <p class="person__title">manager</p>
    </div>

    <div class="contacts">
      <span class="contacts__item contacts__item--wide">
        <svg class="contacts__icon" viewBox="0 0 12 12"><path d="M6 1 0 6h2v5h3V8h2v3h3V6h2z"/></svg>
        PO Box 2817, Brackenvale Qld 4215
      </span>
      <span class="contacts__item">
        <svg class="contacts__icon" viewBox="0 0 12 12"><rect x="3" y="0" width="6" height="12" rx="1"/><rect x="4" y="1.5" width="4" height="6" fill="#f6f7f8"/></svg>
        0419 358 027
      </span>
      <span class="contacts__item">
        <svg class="contacts__icon" viewBox="0 0 12 12"><path d="M2 0h3l1 3-2 1.5a7 7 0 0 0 3.5 3.5L9 6l3 1v3a2 2 0 0 1-2 2A10 10 0 0 1 0 2a2 2 0 0 1 2-2z"/></svg>
        1300 582 914
      </span>
      <span class="contacts__item">
        <svg class="contacts__icon" viewBox="0 0 12 12"><rect x="3" y="0" width="6" height="4"/><rect x="0" y="4" width="12" height="5"/><rect x="3" y="8" width="6" height="4"/></svg>
        1300 582 917
      </span>
      <span class="contacts__item">
        <svg class="contacts__icon" viewBox="0 0 12 12"><circle cx="6" cy="6" r="5" fill="none" stroke="#8c1538" stroke-width="1.4"/><path d="M1 6h10M6 1c-3 3-3 7 0 10M6 1c3 3 3 7 0 10" fill="none" stroke="#8c1538" stroke-width="1"/></svg>
        www.selwickgroup.com.au
      </span>
      <span class="contacts__item contacts__item--wide">
        <svg class="contacts__icon" viewBox="0 0 12 12"><rect x="0" y="2" width="12" height="8"/><path d="M0 2l6 5 6-5" fill="none" stroke="#f6f7f8" stroke-width="1.2"/></svg>
        e: admin@selwickgroup.com.au
      </span>
    </div>
    <div class="band"></div>
  </section>

  <section class="card card--back" aria-label="Business card back">
    <div class="ghost-mark"></div>
    <div class="wordmark">
      <span class="wordmark__dot"></span>
      <span class="wordmark__name">The Selwick Group</span>
    </div>
    <div class="wordmark-rule"></div>
    <p class="tagline">Property Development<span class="tagline__sep">|</span>Premium Accommodation</p>
  </section>

</main>
</body>
</html>
```